Innovative Educational Technology Startup needs Business Cards!

"Scholar Horizon" is an all-in-one, social profile based, online portal for Companies and Students to connect and carry out their brand ambassadorship tasks and requirements. The service allows for companies to more efficiently deploy brand ambassadorship opportunities to the millions of students actively seeking on-campus work experience.

Both educational and corporate tied into one (please keep that in mind for design purposes)
Updates

Project Deadline Extended
Reason: Need time to provide feedback to the several great designs that have been created! Thanks for the patience of one more day!

Target Market(s)

Those who get the card will more than likely be business men and working adults, but many educational instructors, professors, students, marketers, and propoective collegiate students will be the main target for these cards.

Industry/Entity Type

Business

Requirements
Must have
• Our Icon-Sized Logo (SH) must be a focus in regards to imagery.
• Color scheme must be Tiffany Blue/Black/White..(base of the card either white or black).
• www.scholarhorizonhub.com located somewhere on it, but not the main point of the card. (Logo is for that)
Should not have
• Childish or Tech-Only appeal.
• Basic font.
• Rather there be as little asymmetry in the card shape as possible. (curved edges is fine)

```html
<!DOCTYPE html>
<html lang="en">
<head>
<meta charset="utf-8">
<title>Scholar Horizon – Business Card</title>
<link rel="stylesheet" href="https://fonts.googleapis.com/css2?family=Ubuntu:wght@400;500;700&display=swap">
<style>
  :root {
    --tiffany: #0aa5dd;
    --ink: #231f20;
    --text: #3a3a3a;
    --card: #f7f7f7;
    --stage: #e4e4e4;
  }
  * { box-sizing: border-box; margin: 0; padding: 0; }
  html, body {
    width: 1200px; height: 900px; overflow: hidden;
    background: var(--stage);
    font-family: "Ubuntu", sans-serif;
  }
  .card {
    position: absolute;
    left: 337px;
    width: 525px; height: 300px;
    background: var(--card);
    box-shadow: 0 2px 6px rgba(0,0,0,.12);
    overflow: hidden;
  }
  .card--back { top: 80px; }
  .card--front { top: 500px; }

  .brand {
    display: flex; align-items: center; gap: 12px;
  }
  .brand__mark {
    width: 34px; height: 34px;
    background: var(--tiffany);
  }
  .brand__name {
    font-weight: 400;
    color: var(--ink);
    letter-spacing: .5px;
  }
  .card--back .brand {
    position: absolute; left: 0; right: 0; top: 128px;
    justify-content: center;
  }
  .card--back .brand__name { font-size: 28px; }

  .edge { position: absolute; top: 0; height: 300px; width: 30px; }
  .edge--left { left: 0; }
  .edge--right { right: 0; }

  .card--front .brand {
    position: absolute; left: 72px; top: 46px;
  }
  .card--front .brand__name { font-size: 26px; }

  .person {
    position: absolute; left: 78px; top: 180px;
  }
  .person__name {
    color: var(--tiffany); font-weight: 700; font-size: 15px; letter-spacing: .4px;
  }
  .person__title {
    color: var(--text); font-size: 15px; margin-top: 1px;
  }

  .contact {
    position: absolute; left: 265px; top: 118px;
    list-style: none; color: var(--text); font-size: 14px; line-height: 18px;
  }
  .contact__item { display: flex; align-items: flex-start; gap: 12px; }
  .contact__item--address { margin-bottom: 14px; }
  .contact__icon { width: 14px; height: 14px; margin-top: 2px; flex: none; fill: var(--tiffany); }
</style>
</head>
<body>

<section class="card card--back" aria-label="Card back">
  <div class="brand">
    <span class="brand__mark"></span>
    <span class="brand__name">Scholar Horizon</span>
  </div>
</section>

<section class="card card--front" aria-label="Card front">
  <svg class="edge edge--left" viewBox="0 0 30 300" preserveAspectRatio="none">
    <polygon points="0,0 14,0 30,148 30,152 0,136" fill="var(--tiffany)"/>
    <polygon points="0,146 30,162 30,300 0,300" fill="var(--ink)"/>
  </svg>
  <svg class="edge edge--right" viewBox="0 0 30 300" preserveAspectRatio="none">
    <polygon points="0,0 30,0 30,126 0,150" fill="var(--ink)"/>
    <polygon points="0,160 30,136 30,300 16,300 0,290" fill="var(--tiffany)"/>
  </svg>

  <div class="brand">
    <span class="brand__mark"></span>
    <span class="brand__name">Scholar Horizon</span>
  </div>

  <div class="person">
    <p class="person__name">DANIEL REYES</p>
    <p class="person__title">President</p>
  </div>

  <ul class="contact">
    <li class="contact__item contact__item--address">
      <svg class="contact__icon" viewBox="0 0 14 14"><path d="M7 0a5 5 0 0 0-5 5c0 3.6 5 9 5 9s5-5.4 5-9a5 5 0 0 0-5-5zm0 7a2 2 0 1 1 0-4 2 2 0 0 1 0 4z"/></svg>
      <span>000 Harbor Crest Ave Suite 000<br>Lakeview, CA 90000</span>
    </li>
    <li class="contact__item">
      <svg class="contact__icon" viewBox="0 0 14 14"><path d="M1 5c0-2 3-3 6-3s6 1 6 3v1h-3V5H4v1H1zM3 7h8l1 5H2z"/></svg>
      <span>000 000 0000</span>
    </li>
    <li class="contact__item">
      <svg class="contact__icon" viewBox="0 0 14 14"><path d="M4 0h6a1 1 0 0 1 1 1v12a1 1 0 0 1-1 1H4a1 1 0 0 1-1-1V1a1 1 0 0 1 1-1zm1 2v4h4V2z"/></svg>
      <span>000 000 0000</span>
    </li>
    <li class="contact__item">
      <svg class="contact__icon" viewBox="0 0 14 14"><path d="M0 3h14v9H0zm1.5 1 5.5 4 5.5-4v-.2H1.5z" fill-rule="evenodd"/></svg>
      <span>name@scholarhorizonhub.com</span>
    </li>
  </ul>
</section>

</body>
</html>
```